Quiet Sunrise. a calm way of living.

adding value to ones circumstance through the teachings of neutralization. quote for back of card: "and then it happens... One day you wake up and you're in this place. You are in this place where everything is right. Your heart is calm. Your soul is lit. Your thoughts are positive. Your vision is clear. Your faith is stronger than ever. And you are at peace. At peace with where you have been. At peace with what you've been through. And at peace with where you're headed." -unknown

Target Market(s)

spiritual, awakening, inspiration, motivation, gratefulness, oneness, peace, positive mindset,

Contact Information for Business Card

front: one line message from quote

Logo Text

up to suggestions

Font styles to use
Serif
Sans Serif
Script

Colors

Designer to choose colors to be used in the design.

Requirements
Must have
• entire quote on one side of card
Nice to have
• simple, and to the point
Should not have
• elaborated designs

```html
<!DOCTYPE html>
<html lang="en">
<head>
<meta charset="utf-8">
<title>Quiet Sunrise — Business Card</title>
<link href="https://fonts.googleapis.com/css2?family=Cabin:wght@400;500&family=Montserrat:wght@500;700&display=swap" rel="stylesheet">
<style>
  :root {
    --backdrop: #2a2a2c;
    --card: #2f4562;
    --accent: #e9e43a;
    --ink: #ffffff;
  }
  * { margin: 0; padding: 0; box-sizing: border-box; }
  html, body {
    width: 1200px; height: 902px; overflow: hidden;
    background: var(--backdrop);
  }
  .stage { position: relative; width: 1200px; height: 902px; }
  .card {
    position: absolute;
    width: 620px; height: 354px;
    background: var(--card);
    box-shadow: 0 14px 30px rgba(0,0,0,0.45);
  }
  .card--back { left: 60px; top: 70px; padding: 62px 46px 0 50px; }
  .quote {
    font-family: "Cabin", sans-serif;
    font-size: 19.5px;
    line-height: 1.5;
    letter-spacing: 0.2px;
    color: var(--accent);
  }
  .card--front { left: 520px; top: 470px; }
  .brand {
    position: absolute; left: 40px; top: 118px;
    font-family: "Montserrat", sans-serif;
    font-weight: 500;
  }
  .brand__name {
    font-size: 30px; line-height: 1.2;
    color: var(--ink);
  }
  .brand__tagline {
    font-size: 20px; line-height: 1.4;
    color: var(--accent);
    margin-top: 4px;
  }
  .contact {
    position: absolute; right: 40px; top: 200px;
    text-align: right;
    font-family: "Montserrat", sans-serif;
    font-weight: 500; font-size: 16px; line-height: 1.45;
    color: var(--accent);
  }
  .person {
    position: absolute; left: 40px; bottom: 40px;
    font-family: "Montserrat", sans-serif;
    line-height: 1.15;
  }
  .person__name { font-weight: 700; font-size: 21px; color: var(--ink); }
  .person__role { font-weight: 500; font-size: 17px; color: var(--accent); }
</style>
</head>
<body>
<main class="stage">
  <section class="card card--back">
    <p class="quote">And then it happens… One day you wake up and you're in this place. You are in this place where everything is right. Your heart is calm. Your soul is lit. Your thoughts are positive. Your vision is clear. Your faith is stronger than ever. And you are at peace. At peace with where you have been. At peace with what you've been through. And at peace with where you're headed.</p>
  </section>

  <section class="card card--front">
    <div class="brand">
      <div class="brand__name">Quiet Sunrise</div>
      <div class="brand__tagline">a calm way of living</div>
    </div>
    <div class="contact">
      <div>+34 900 123 456</div>
      <div>hello@quietsunrise.com</div>
    </div>
    <div class="person">
      <div class="person__name">DANIEL MARSH</div>
      <div class="person__role">MANAGING DIRECTOR</div>
    </div>
  </section>
</main>
</body>
</html>
```